Brennick Holdings Business Cards

These are professional business cards that are for my family office.
Put fake emails and phone numbers as of now until I finalize those components. This family office controls my families investments, assets, and future. The cards should be professional.
..
.
.
.
I just uploaded another variation of a logo I would like to see as a business card to I am inbeteen which logo to use

Target Market(s)

business

Industry/Entity Type

business

Contact Information for Business Card

Professional, wealth related, finance related.

Requirements
Must have
• Logo

```html
<!DOCTYPE html>
<html lang="en">
<head>
<meta charset="utf-8">
<title>Brennick Holdings — Business Cards</title>
<link href="https://fonts.googleapis.com/css2?family=Montserrat:wght@400;500;700&family=Lato:wght@400&display=swap" rel="stylesheet">
<style>
  :root {
    --backdrop: #2a2a2c;
    --navy: #161c2a;
    --white: #ffffff;
    --silver: #c9ccd2;
    --soft: #d9dce2;
  }
  html, body {
    margin: 0;
    padding: 0;
    width: 1200px;
    height: 689px;
    overflow: hidden;
    background: var(--backdrop);
  }
  .canvas {
    position: relative;
    width: 1200px;
    height: 689px;
  }
  .card {
    position: absolute;
    top: 194px;
    width: 525px;
    height: 300px;
    border-radius: 16px;
    background: var(--navy);
    overflow: hidden;
    box-shadow: 0 14px 30px rgba(0,0,0,.35);
  }
  .card--front { left: 45px; }
  .card--back  { left: 630px; }

  .brand {
    display: flex;
    align-items: center;
    gap: 12px;
    font-family: "Montserrat", sans-serif;
    font-weight: 500;
    text-transform: uppercase;
    letter-spacing: 3px;
  }
  .brand__dot {
    width: 14px;
    height: 14px;
    border-radius: 50%;
    background: currentColor;
  }
  .card--front .brand {
    position: absolute;
    left: 0; right: 0; top: 0; bottom: 0;
    justify-content: center;
    color: var(--silver);
    font-size: 24px;
  }

  .emblem-ring {
    position: absolute;
    left: 0; top: 0;
  }
  .emblem {
    position: absolute;
    left: 282px;
    top: -28px;
    width: 290px;
    height: 290px;
    border-radius: 50%;
    background: var(--white);
    display: flex;
    align-items: center;
    justify-content: center;
  }
  .emblem .brand {
    flex-direction: column;
    gap: 10px;
    color: var(--navy);
    font-size: 17px;
    letter-spacing: 2.5px;
    text-align: center;
    margin-left: -8px;
    margin-top: 10px;
  }

  .holder {
    position: absolute;
    left: 34px;
    top: 152px;
    color: var(--white);
    font-family: "Montserrat", sans-serif;
  }
  .holder__name {
    margin: 0;
    font-size: 21px;
    font-weight: 700;
    letter-spacing: .5px;
    text-transform: uppercase;
  }
  .holder__title {
    margin: 2px 0 0;
    font-family: "Lato", sans-serif;
    font-size: 11.5px;
    color: var(--soft);
  }
  .contact {
    list-style: none;
    margin: 12px 0 0;
    padding: 0;
    font-family: "Lato", sans-serif;
    font-size: 10.5px;
    line-height: 1.35;
    color: var(--soft);
  }
  .contact li {
    display: flex;
    align-items: flex-start;
    gap: 8px;
    margin-bottom: 2px;
  }
  .contact svg {
    flex: none;
    width: 10px;
    height: 10px;
    margin-top: 2px;
    fill: var(--white);
  }
</style>
</head>
<body>
<main class="canvas">

  <section class="card card--front" aria-label="Card front">
    <div class="brand"><span class="brand__dot"></span>Brennick Holdings</div>
  </section>

  <section class="card card--back" aria-label="Card back">
    <svg class="emblem-ring" width="525" height="300" viewBox="0 0 525 300" aria-hidden="true">
      <circle cx="427" cy="117" r="160" fill="none" stroke="#ffffff" stroke-width="2"/>
    </svg>
    <div class="emblem">
      <div class="brand"><span class="brand__dot"></span>Brennick<br>Holdings</div>
    </div>

    <div class="holder">
      <h1 class="holder__name">Daniel Harlow</h1>
      <p class="holder__title">Founder &amp; CEO</p>
      <ul class="contact">
        <li>
          <svg viewBox="0 0 10 10"><path d="M5 0a3.5 3.5 0 0 0-3.5 3.5C1.5 6 5 10 5 10s3.5-4 3.5-6.5A3.5 3.5 0 0 0 5 0zm0 5a1.5 1.5 0 1 1 0-3 1.5 1.5 0 0 1 0 3z"/></svg>
          <span>423 Street Address Here, City<br>State &amp; Country, ZIP Code</span>
        </li>
        <li>
          <svg viewBox="0 0 10 10"><path d="M2 0l2 2.4-1 1.2a6 6 0 0 0 3.4 3.4l1.2-1L10 8l-1 2C4 10 0 6 0 1z"/></svg>
          <span>(123) 456-7890</span>
        </li>
        <li>
          <svg viewBox="0 0 10 10"><path d="M2.5 0h5a1 1 0 0 1 1 1v8a1 1 0 0 1-1 1h-5a1 1 0 0 1-1-1V1a1 1 0 0 1 1-1zm0 1.2v6.6h5V1.2z"/></svg>
          <span>(123) 456-7890</span>
        </li>
        <li>
          <svg viewBox="0 0 10 10"><path d="M2.5 0h5v3h-5zM0 3.5h10v4H8V10H2V7.5H0zm3 3v2.5h4V6.5z"/></svg>
          <span>(123) 456-7890</span>
        </li>
        <li>
          <svg viewBox="0 0 10 10"><path d="M0 1.5h10v7H0zm1 1v.3l4 2.6 4-2.6v-.3z"/></svg>
          <span>info@yourwebsitehere.com</span>
        </li>
        <li>
          <svg viewBox="0 0 10 10"><circle cx="5" cy="5" r="5"/></svg>
          <span>yourwebsitehere.com</span>
        </li>
      </ul>
    </div>
  </section>

</main>
</body>
</html>
```